Mortgage firm needs clean and simple wordpress website and logo

The competition is for design only, and the winning design for the homepage will be expected to create a second design for a simpler template for additional pages.

We need a logo and basic wordpress website design for a Sydney based mortgage firm.
We need a clean and simple logo and website, based on the mortgage/accounting/finance/tax industry. Simple, credible and official colors.

The logo is expected to be so simple that we have combined into the one job.
If you submit a logo design and we choose it along with someone else's website design you will be paid a bonus of $60. The website design will still win the competition as per normal.

Current website is old and terrible but gives you an idea of the sitemap (super simple) and what they do: http://www.lendbridgeloans.com.au/

We will integrate a mortgage calculator into the site.
The calculator is adjustable in styles, you can see it here: http://www.lendbridgeloans.com.au/mortgagecalculator/

We want original different to copy-and-paste template looking designs.
We like simple websites with a long home page and a few additional pages like https://www.homefundpath.com.au/

We are based in Sydney Australia and are mortgage brokers

We want a clean, formal, credible site, limited pages.

The project is guaranteed, so go for it.

Example of basic template after home page complete: http://lendbridgeloans.com.au/template_example.jpg

Target Market(s)

Mortgage and banking clients

Industry/Entity Type

Finance

Number of Pages Required

1 page

Requirements
Must have
• A simple logo, Wordpress capable, be able to incorporate the mortgage calculator (on the home page if needed as well as its own page)
Nice to have
• VIdeo - something free but nice

```html
<!DOCTYPE html>
<html lang="en">
<head>
<meta charset="utf-8">
<title>Lendbridge Loans – Private Funding</title>
<link href="https://fonts.googleapis.com/css2?family=Open+Sans:wght@300;400;600;700&display=swap" rel="stylesheet">
<style>
:root{
  --blue:#2f7fd0;
  --dark:#2b2b2b;
  --text:#333;
  --muted:#777;
  --light-bg:#f7f7f7;
  --footer-bg:#f2f2f2;
  --line:#e3e3e3;
  --white:#fff;
  --hero-a:#3c4658;
  --hero-b:#5a5e5c;
}
*{box-sizing:border-box;margin:0;padding:0}
html,body{width:802px;height:1200px;overflow:hidden}
body{font-family:"Open Sans",Arial,sans-serif;color:var(--text);background:var(--white);position:relative}
.abs{position:absolute}
/* hero */
.hero{position:absolute;left:0;top:0;width:802px;height:410px;overflow:hidden}
.hero-photo{position:absolute;inset:0;background:linear-gradient(180deg,#34405a 0%,#4b5566 45%,#5e5d58 80%,#4a4a48 100%)}
.hero-shade{position:absolute;inset:0;background:rgba(0,0,0,.25)}
.brand{position:absolute;left:88px;top:14px;color:var(--white)}
.brand-name{font-size:21px;font-weight:600;letter-spacing:.3px;line-height:28px}
.brand-tag{font-size:8px;font-weight:600;text-align:right;letter-spacing:.3px;margin-top:-3px}
.nav{position:absolute;right:88px;top:37px;display:flex;gap:19px;font-size:7.5px;color:rgba(255,255,255,.8)}
.nav .active{color:var(--white);position:relative}
.nav .active svg{position:absolute;left:50%;top:-16px;transform:translateX(-50%)}
.header-rule{position:absolute;left:0;top:70px;width:802px;height:1px;background:rgba(255,255,255,.3)}
.play{position:absolute;left:386px;top:159px}
.hero-title{position:absolute;left:0;top:198px;width:802px;text-align:center;color:var(--white);font-size:17px;font-weight:700}
.hero-sub{position:absolute;left:200px;top:220px;width:402px;text-align:center;color:var(--white);font-size:16px;font-weight:300;line-height:22px}
.hero-btn{position:absolute;left:345px;top:276px;width:112px;height:31px;border:1.5px solid var(--white);border-radius:3px;color:var(--white);font-size:12.5px;display:flex;align-items:center;justify-content:center}
/* calculator */
.calc{position:absolute;left:0;top:410px;width:802px;height:236px;background:var(--light-bg)}
.calc-title{position:absolute;left:0;top:24px;width:802px;text-align:center;color:var(--blue);font-size:22px;font-weight:600}
.field{position:absolute;width:146px}
.field-label{font-size:9.5px;color:var(--text)}
.range-ends{display:flex;justify-content:space-between;font-size:7.5px;margin-top:5px}
.track{position:relative;height:3px;background:#d6d6d6;margin-top:3px}
.track .fill{position:absolute;left:0;top:0;height:3px;background:var(--blue)}
.track .knob{position:absolute;top:-2px;width:7px;height:7px;border-radius:50%;background:#333;margin-left:-3.5px}
.value{position:absolute;top:20px;font-size:7.5px;background:var(--white);border:1px solid #ccc;border-radius:2px;padding:2px 6px;transform:translateX(-50%)}
.select{position:absolute;top:170px;width:146px;height:29px;background:var(--white);border:1px solid #ccc;font-size:8px;display:flex;align-items:center;justify-content:space-between;padding:0 10px}
.btn{position:absolute;top:170px;height:29px;background:var(--dark);color:var(--white);font-size:8px;display:flex;align-items:center;justify-content:center;gap:4px}
.up{position:absolute;left:392px;top:227px}
/* features */
.feature{position:absolute;top:692px;width:190px}
.feature h3{position:absolute;left:46px;top:0;font-size:16px;font-weight:500;color:var(--text);white-space:nowrap}
.feature p{position:absolute;left:47px;top:29px;width:140px;font-size:6.6px;line-height:12px;color:var(--muted)}
.feature svg{position:absolute;left:0;top:4px}
.rule{position:absolute;left:0;top:821px;width:802px;height:1px;background:var(--line)}
/* testimonials */
.testi-title{position:absolute;left:0;top:860px;width:802px;text-align:center;font-size:15px;font-weight:500}
.side-card{position:absolute;top:890px;width:94px;height:111px}
.side-card.left{left:72px;background:linear-gradient(90deg,rgba(255,255,255,1),#eee)}
.side-card.right{left:626px;background:linear-gradient(90deg,#eee,rgba(255,255,255,1))}
.card{position:absolute;left:180px;top:890px;width:432px;height:111px;border:1px solid #ccc;border-radius:2px;background:var(--white)}
.quote{position:absolute;left:16px;top:19px;width:400px;text-align:center;font-size:7.5px;line-height:13px;color:#555}
.author{position:absolute;left:0;top:68px;width:432px;text-align:center;font-size:8.5px;color:#555}
.avatar{position:absolute;left:382px;top:982px;width:38px;height:38px;border-radius:50%;border:2px solid #ddd;background:radial-gradient(circle,#b99b85,#7c6758)}
.arrow{position:absolute;top:938px}
/* footer */
.footer{position:absolute;left:0;top:1070px;width:802px;height:130px;background:var(--footer-bg)}
.contact{position:absolute;top:22px;font-size:7.5px;color:var(--text)}
.contact b{display:block;font-size:9.5px;font-weight:400;margin-top:1px}
.contact svg{vertical-align:-1px;margin-right:2px}
.footer-rule{position:absolute;left:88px;top:64px;width:626px;height:1px;background:#ddd}
.footer-links{position:absolute;left:88px;top:82px;font-size:6.8px;color:#555}
.footer-links span{margin:0 5px;color:#999}
.copyright{position:absolute;left:88px;top:100px;font-size:6.8px;color:#555}
.social{position:absolute;top:88px;width:17px;height:17px;border-radius:50%;background:#aaa}
</style>
</head>
<body>

<section class="hero">
  <div class="hero-photo" role="img" aria-label="Background video still: city towers seen through a tall colonnade with people walking"></div>
  <div class="hero-shade"></div>
  <div class="brand">
    <div class="brand-name">Lendbridge Loans</div>
    <div class="brand-tag">PRIVATE FUNDING</div>
  </div>
  <nav class="nav">
    <span class="active"><svg width="9" height="8" viewBox="0 0 10 9"><path d="M5 0 10 4.5H8.5V9H6V6H4v3H1.5V4.5H0z" fill="#fff"/></svg>HOME</span>
    <span>ABOUT US</span><span>SERVICES</span><span>MORTGAGE CALCULATOR</span><span>CONTACT US</span>
  </nav>
  <div class="header-rule"></div>
  <svg class="play" width="30" height="30" viewBox="0 0 30 30"><circle cx="15" cy="15" r="15" fill="rgba(255,255,255,.55)"/><path d="M11 8 22 15 11 22z" fill="#555"/></svg>
  <h1 class="hero-title">Home, investment and commercial loans</h1>
  <p class="hero-sub">for purchase, refinance and consolidation at up to 80% lending.</p>
  <div class="hero-btn">Contact Us</div>
</section>

<section class="calc">
  <h2 class="calc-title">Mortgage Calculator</h2>

  <div class="field" style="left:124px;top:72px">
    <div class="field-label">Loan Amount</div>
    <div class="range-ends"><span>$0</span><span>$100000</span></div>
    <div class="track"><div class="fill" style="width:44px"></div><div class="knob" style="left:44px"></div><div class="value" style="left:44px">$10000</div></div>
  </div>
  <div class="field" style="left:327px;top:72px">
    <div class="field-label">Loan Term</div>
    <div class="range-ends"><span>0</span><span>30 Years</span></div>
    <div class="track"><div class="fill" style="width:45px"></div><div class="knob" style="left:45px"></div><div class="value" style="left:45px">7 Years</div></div>
  </div>
  <div class="field" style="left:530px;top:72px">
    <div class="field-label">Loan Interest</div>
    <div class="range-ends"><span>0%</span><span>70%</span></div>
    <div class="track"><div class="fill" style="width:45px"></div><div class="knob" style="left:45px"></div><div class="value" style="left:45px">28%</div></div>
  </div>

  <div class="field-label abs" style="left:124px;top:152px">Repayment Type</div>
  <div class="field-label abs" style="left:328px;top:152px">Repayment Frequency</div>
  <div class="select" style="left:124px">Principal and Interest<svg width="7" height="5" viewBox="0 0 7 5"><path d="M.5 .5 3.5 3.5 6.5 .5" stroke="#333" fill="none"/></svg></div>
  <div class="select" style="left:328px">monthly<svg width="7" height="5" viewBox="0 0 7 5"><path d="M.5 .5 3.5 3.5 6.5 .5" stroke="#333" fill="none"/></svg></div>
  <div class="btn" style="left:532px;width:70px"><svg width="7" height="8" viewBox="0 0 7 8"><rect x=".5" y=".5" width="6" height="7" fill="none" stroke="#fff"/><rect x="1.5" y="1.5" width="4" height="1.5" fill="#fff"/></svg>Calculate</div>
  <div class="btn" style="left:606px;width:71px"><svg width="9" height="7" viewBox="0 0 9 7"><path d="M0 7V0M0 7H9L9 2 6 4 4 1 1 5V7" fill="#fff" stroke="#fff" stroke-width=".8"/></svg>View Chart</div>

  <svg class="up" width="18" height="18" viewBox="0 0 18 18"><circle cx="9" cy="9" r="9" fill="#666"/><path d="M5 11 9 7 13 11" stroke="#fff" stroke-width="2" fill="none"/></svg>
</section>

<section>
  <div class="feature" style="left:88px">
    <svg width="36" height="34" viewBox="0 0 36 34" fill="none" stroke="#2f7fd0" stroke-width="1.4"><rect x="1" y="4" width="34" height="29"/><path d="M1 11H35M9 1V7M27 1V7M5 16H31V29H5zM11.5 16V29M18 16V29M24.5 16V29M5 20.5H31M5 25H31"/></svg>
    <h3>Experience</h3>
    <p>Our team has been arranging and managing finance for clients for over 25 years using our access to banks, private lenders and brokers within Australia.</p>
  </div>
  <div class="feature" style="left:308px">
    <svg width="34" height="34" viewBox="0 0 34 34" fill="none" stroke="#2f7fd0" stroke-width="1.4"><circle cx="17" cy="17" r="16"/><path d="M17 6V17L24 24"/><path d="M17 3V5M17 29V31M3 17H5M29 17H31" /></svg>
    <h3>Fast</h3>
    <p>We can provide money in 24 Hours, providing you meet the loan criteria. Unlike banks that might take months to complete a loan, we can react to your demands quickly.</p>
  </div>
  <div class="feature" style="left:532px">
    <svg width="32" height="36" viewBox="0 0 32 36" fill="none" stroke="#2f7fd0" stroke-width="1.4"><path d="M7 15V10a9 9 0 0 1 18 0v5M11 15V10a5 5 0 0 1 10 0v5"/><rect x="1" y="15" width="30" height="19"/><path d="M1 22H31M1 30H31M5 30 10 22M11 30 16 22M17 30 22 22M23 30 28 22"/></svg>
    <h3>Private</h3>
    <p>Our specialty is private lending for residential, commercial and industrial properties. We generally look for registered first mortgage security with up to 80% loan funding based on the property valuation, the type of security and the borrower profile.</p>
  </div>
</section>
<div class="rule"></div>

<section>
  <h2 class="testi-title">Testimonials</h2>
  <div class="side-card left"></div>
  <div class="side-card right"></div>
  <svg class="arrow" style="left:89px" width="8" height="14" viewBox="0 0 8 14"><path d="M7 1 1 7 7 13" stroke="#bbb" stroke-width="1.3" fill="none"/></svg>
  <svg class="arrow" style="left:705px" width="8" height="14" viewBox="0 0 8 14"><path d="M1 1 7 7 1 13" stroke="#bbb" stroke-width="1.3" fill="none"/></svg>
  <div class="card">
    <p class="quote"><svg width="12" height="9" viewBox="0 0 12 9" style="vertical-align:0;margin-right:4px"><path d="M0 9V4Q0 0 4 0V2Q2 2 2 4H5V9zM7 9V4Q7 0 11 0V2Q9 2 9 4H12V9z" fill="#aaa"/></svg>Cras blandit ipsum vitae laoreet dapibus. Aenean a sodales nisi, in vestibulum purus. Lorem ipsum dolor sit amet, consectetur adipiscing elit. Pellentesque ultrices, sapien sit amet facilisis condimentum, ex sem dictum odio, at placerat ex sem eget purus.<svg width="12" height="9" viewBox="0 0 12 9" style="vertical-align:-6px;margin-left:4px"><path d="M12 0V5Q12 9 8 9V7Q10 7 10 5H7V0zM5 0V5Q5 9 1 9V7Q3 7 3 5H0V0z" fill="#aaa"/></svg></p>
    <div class="author">~ Peter Walsh</div>
  </div>
  <div class="avatar" role="img" aria-label="Client portrait photo"></div>
</section>

<footer class="footer">
  <div class="contact" style="left:88px"><svg width="7" height="7" viewBox="0 0 7 7"><circle cx="3.5" cy="2" r="2" fill="#333"/><path d="M0 7Q0 4 3.5 4T7 7z" fill="#333"/></svg>Daniel K. Marsh<b>+614 1555 0142</b></div>
  <div class="contact" style="left:210px"><svg width="7" height="7" viewBox="0 0 7 7"><circle cx="3.5" cy="2" r="2" fill="#333"/><path d="M0 7Q0 4 3.5 4T7 7z" fill="#333"/></svg>Oliver T. Grant<b>+614 1555 0178</b></div>
  <div class="contact" style="left:337px"><svg width="7" height="7" viewBox="0 0 7 7"><path d="M1 0 2.5 0 3 2 2 3Q3 5 4 5L5 4 7 4.5 7 6Q6 7 5 7 0 6 0 1Q0 0 1 0z" fill="#333"/></svg>Office<b>+612 9555 0120</b></div>
  <div class="contact" style="left:455px"><svg width="7" height="7" viewBox="0 0 7 7"><rect x="0" y="2.5" width="7" height="4.5" fill="#333"/><rect x="1.5" y="0" width="4" height="3" fill="#333"/></svg>Fax<b>+612 9555 0121</b></div>
  <div class="contact" style="left:566px"><svg width="8" height="6" viewBox="0 0 8 6"><rect width="8" height="6" fill="#333"/><path d="M0 0 4 3.5 8 0" stroke="#f2f2f2" fill="none"/></svg>Email<b>info@lendbridgeloans.com.au</b></div>
  <div class="footer-rule"></div>
  <div class="footer-links">Home<span>|</span>About Us<span>|</span>Services<span>|</span>Mortgage Calculator<span>|</span>Contact Us</div>
  <div class="copyright">Copyright © 2016 &nbsp;Company Name. &nbsp;All rights reserved.</div>
  <div class="social" style="left:653px"></div>
  <div class="social" style="left:674px"></div>
  <div class="social" style="left:696px"></div>
</footer>

</body>
</html>
```